Business Card - Professional Minimalist - Double sided

We appreciate minimalist logo/web/collateral designs that allow design to tell a story. We want to relay a professional image/approach but throwing in a splash of modern when we’re able so long as it’s not distracting. Think 75% classic corporate, 25% modern. Open to black or white design, not sure which might look the best.

Target Market(s)

Senior executives or related government affairs contacts within the agriculture, energy, and defense industries (i.e., potential clients) but located outside of Washington, DC. Most potential clients based in DC with be familiar with both of us and our shared history.

Industry/Entity Type

Consulting

Contact Information for Business Card

Name: Derek M. Holloway
Title: Co-Founder & Partner
Address: 418 Linwood Terrace NE | Suite 2260 | Washington, D.C. 20017
Phone: (202) 555-0148
Email: Derek@BrimleyHolloway.example

Font styles to use
Serif

Colors

Designer to choose only greyscale colors for use in the design.

Requirements
Must have
• Name: Derek M. Holloway
Phone: (202) 555-0148

```html
<!DOCTYPE html>
<html lang="en">
<head>
<meta charset="utf-8">
<title>Brimley Holloway Group – Business Card</title>
<link rel="stylesheet" href="https://fonts.googleapis.com/css2?family=Marcellus&family=Montserrat:wght@400;500;700&display=swap">
<style>
  :root {
    --backdrop: #e4e4e4;
    --paper: #ffffff;
    --ink: #2e2e2e;
    --charcoal: #4a4a4a;
    --silver: #a6a6a8;
    --rule: #b8b8b8;
  }
  * { box-sizing: border-box; margin: 0; padding: 0; }
  html, body { width: 1200px; height: 892px; overflow: hidden; }
  body {
    background: var(--backdrop);
    position: relative;
    font-family: "Montserrat", sans-serif;
    color: var(--ink);
  }
  .card {
    position: absolute;
    left: 250px;
    width: 700px;
    height: 400px;
    background: var(--paper);
    overflow: hidden;
    box-shadow: 0 2px 10px rgba(0,0,0,0.12);
  }
  .card--front { top: 26px; }
  .card--back { top: 466px; }

  /* brand lockup */
  .brand { position: absolute; display: flex; align-items: center; gap: 14px; }
  .brand__square { width: 34px; height: 34px; background: var(--charcoal); flex: none; }
  .brand__text { font-family: "Marcellus", serif; color: var(--charcoal); }
  .brand__name { font-size: 30px; letter-spacing: 1.5px; line-height: 1; white-space: nowrap; }
  .brand__rule { height: 1px; background: var(--rule); margin: 6px 0 4px; }
  .brand__group { font-size: 11px; letter-spacing: 8px; text-align: right; color: var(--silver); }

  .card--front .brand { left: 44px; top: 38px; }
  .card--back .brand { right: 40px; bottom: 44px; }

  /* person */
  .person { position: absolute; left: 44px; top: 140px; }
  .person__name { font-weight: 700; font-size: 20px; letter-spacing: 0.5px; text-transform: uppercase; color: var(--charcoal); }
  .person__title { font-size: 11px; letter-spacing: 0.5px; text-transform: uppercase; color: #7a7a7a; margin-top: 4px; }
  .person__rule { width: 40px; height: 2px; background: var(--charcoal); margin-top: 10px; }

  .contact { position: absolute; left: 44px; top: 215px; list-style: none; }
  .contact__item { display: flex; align-items: center; gap: 10px; font-size: 15px; line-height: 26px; }
  .contact__icon { width: 14px; height: 14px; flex: none; }

  .address { position: absolute; left: 44px; bottom: 34px; font-size: 12.5px; letter-spacing: 0.2px; }

  /* decorative blocks */
  .accent { position: absolute; }
  .accent--corner-dark { right: 0; bottom: 0; width: 200px; height: 150px; background: var(--charcoal); }
  .accent--corner-light { right: 0; bottom: 0; width: 150px; height: 105px; background: var(--silver); }
  .accent--band-dark { left: 0; top: 0; width: 56px; height: 400px; background: var(--charcoal); }
  .accent--band-light { left: 56px; top: 0; width: 28px; height: 400px; background: var(--silver); }
</style>
</head>
<body>

  <section class="card card--front" aria-label="Card front">
    <div class="brand">
      <span class="brand__square"></span>
      <div class="brand__text">
        <div class="brand__name">BRIMLEY HOLLOWAY</div>
        <div class="brand__rule"></div>
        <div class="brand__group">GROUP</div>
      </div>
    </div>

    <div class="person">
      <h1 class="person__name">Derek M. Holloway</h1>
      <p class="person__title">Co-Founder &amp; Partner</p>
      <div class="person__rule"></div>
    </div>

    <ul class="contact">
      <li class="contact__item">
        <svg class="contact__icon" viewBox="0 0 14 14"><circle cx="7" cy="7" r="6.3" fill="none" stroke="#4a4a4a" stroke-width="1.2"/><path d="M4.6 3.8l1.3 1.3-.7.9c.5 1 1.3 1.8 2.3 2.3l.9-.7 1.3 1.3-.9 1c-2.4-.4-4.8-2.8-5.2-5.2z" fill="#4a4a4a"/></svg>
        <span>(202) 555-0148</span>
      </li>
      <li class="contact__item">
        <svg class="contact__icon" viewBox="0 0 14 14"><circle cx="7" cy="7" r="6.3" fill="none" stroke="#4a4a4a" stroke-width="1.2"/><rect x="3.8" y="4.8" width="6.4" height="4.4" fill="none" stroke="#4a4a4a" stroke-width="1"/><path d="M3.8 4.8L7 7.4l3.2-2.6" fill="none" stroke="#4a4a4a" stroke-width="1"/></svg>
        <span>Derek@BrimleyHolloway.example</span>
      </li>
      <li class="contact__item">
        <svg class="contact__icon" viewBox="0 0 14 14"><circle cx="7" cy="7" r="6.3" fill="none" stroke="#4a4a4a" stroke-width="1.2"/><ellipse cx="7" cy="7" rx="2.2" ry="4.2" fill="none" stroke="#4a4a4a" stroke-width="0.9"/><path d="M2.8 7h8.4" stroke="#4a4a4a" stroke-width="0.9"/></svg>
        <span>www.BrimleyHolloway.example</span>
      </li>
    </ul>

    <p class="address">418 Linwood Terrace NE | Suite 2260 | Washington, D.C. 20017</p>

    <div class="accent accent--corner-dark"></div>
    <div class="accent accent--corner-light"></div>
  </section>

  <section class="card card--back" aria-label="Card back">
    <div class="accent accent--band-dark"></div>
    <div class="accent accent--band-light"></div>
    <div class="brand">
      <span class="brand__square"></span>
      <div class="brand__text">
        <div class="brand__name">BRIMLEY HOLLOWAY</div>
        <div class="brand__rule"></div>
        <div class="brand__group">GROUP</div>
      </div>
    </div>
  </section>

</body>
</html>
```